Website design for Harbor Bolts. ( Lock company)

Harbor Bolts is a New York Based Company that manufactures a variety of high quality Locks which sell worldwide.

Our website: We need a 'face' on the Internet , a website that tells you who we are and what we do - 'An Identity'.

it is not an eCommerce website . the website is to show customers and potential distributers who we are and what we manufacture ( so they come away with a great impression of our company and our products) see www.quarrymillwheel.com

First glance impression: We are Professional; are locks are strong,and reliable. and we are ready to compete with other major Lock companies

Content: for starters the site will contain general information and background about our company (our story), were to buy our products, contact information, and display images of our Locks (and of course all the classic links including to all the legal and technical information). as time goes on we will add more features to the website i.e. Products, Videos blogs etc.

although at first there will not be that much content on the website - it should not look empty (it should be simple and clear but not empty) it should look and feel like a full fledged professional website (not a template)

Inspiration: here are a few sites which have the feel we are looking for:

General tone - quarrymillwheel.com bantrell.com (black is good - But not a must )

Simplicity, clarity - coolvantix.com hearthmate.com

the widescreen Image look - http://www.layoutgarden.com/demo/81952.html

we are considering perhaps having wide HQ images of Lion(s) in the background (but without the felling that it is a zoo or safari website) - it is not a must, its just an idea .

perhaps (if you find it looks good ) use a bit of that metal or chrome look to give it it a strong smooth feel (however it should not look like a dark prison)

We do not currently have a Logo ( if you feel you can design one that fits the above company description - we would love to see if it can work for us) We can talk about additional funds for the logo during this project.

Our working slogan is : Harbor Bolts - "Keeper of the Gate"

for your convenience we have attached a few images of the type of locks we sell

We are looking to collaborate with you throughout the project. We have ideas and visions we want implemented and we will help you along the way. So we can create the perfect website.

Thank you.

```html
<!DOCTYPE html>
<html lang="en">
<head>
<meta charset="utf-8">
<title>Harbor Bolts - Keeper of the Gate</title>
<link rel="stylesheet" href="https://fonts.googleapis.com/css2?family=Oswald:wght@300;400;500;700&family=Teko:wght@500;600&family=Arimo:wght@400&display=swap">
<style>
:root{
  --black:#000;
  --red:#b40000;
  --red-band:#a70000;
  --red-dark:#6d0000;
  --steel:#5e6268;
  --steel-light:#8a8e94;
  --band:#33363b;
  --text-muted:#7d8187;
  --text-light:#c9ccd0;
  --footer:#222;
  --line:#3b3e42;
}
*{box-sizing:border-box;margin:0;padding:0}
html,body{width:1093px;height:1200px;overflow:hidden;background:var(--black)}
body{position:relative;font-family:"Arimo",Arial,sans-serif;color:var(--text-muted)}
.abs{position:absolute}

.top-strip{left:0;top:0;width:1093px;height:7px;background:var(--red)}
.top-strip::after{content:"";position:absolute;left:666px;top:7px;border:7px solid transparent;border-top-color:var(--red);border-bottom:0}
.site-header{left:0;top:7px;width:1093px;height:60px;border-bottom:1px solid #8d8f92}
.brand{display:flex;align-items:center;gap:8px}
.brand-dot{width:30px;height:30px;border-radius:50%;background:var(--steel-light)}
.brand-name{font-family:"Oswald",sans-serif;font-weight:500;font-size:30px;letter-spacing:0;line-height:1;color:var(--steel-light);text-transform:uppercase}
.site-header .brand{left:119px;top:13px}
.main-nav{right:114px;top:22px;display:flex;gap:14px;font-family:"Oswald",sans-serif;font-size:13px;text-transform:uppercase;color:var(--text-light)}
.main-nav .active::after{content:"";position:absolute;left:668px;top:37px}
.nav-marker{left:666px;top:59px;border:7px solid transparent;border-bottom-color:#8d8f92;border-top:0}

.hero-photo{left:496px;top:67px;width:395px;height:390px;background:linear-gradient(90deg,#050505 0%,#1f2124 30%,#2a2c30 45%,#e9ecef 60%,#1a1b1d 75%,#0a0a0a 100%)}
.hero-copy{left:217px;top:158px;font-family:"Teko",sans-serif;font-weight:600;color:var(--steel);text-transform:uppercase;line-height:.9}
.hero-copy .l1{font-size:27px;font-weight:500}
.hero-copy .l2{font-size:44px}
.hero-copy .l3{font-size:80px;line-height:.82}
.hero-copy .l4{font-size:72px;line-height:.85}

.product-band{left:0;top:457px;width:1093px;height:279px;background:var(--band)}
.product-strip{left:141px;top:476px;width:815px;height:241px;background:var(--black);display:flex;padding:0 8px}
.product{width:200px;text-align:center;padding-top:20px}
.product-image{width:150px;height:118px;margin:0 auto;border-radius:6px}
.product-image.knob{background:radial-gradient(circle at 45% 50%,#f4d98a,#c9972f 60%,#3a2a10 100%)}
.product-image.box{width:64px;background:linear-gradient(180deg,#9a9ea3 0%,#9a9ea3 35%,#2a2b2d 36%,#0f0f10 100%)}
.product-title{margin-top:20px;font-family:"Teko",sans-serif;font-weight:500;font-size:27px;line-height:1;color:var(--red);text-transform:uppercase}
.product-text{margin:6px 0 0 12px;text-align:left;font-size:11px;line-height:13.5px;color:var(--text-muted)}
.carousel-btn{top:584px;width:30px;height:30px}

.welcome-title{left:128px;top:810px;font-family:"Teko",sans-serif;font-weight:600;font-size:52px;line-height:1;color:var(--steel);text-transform:uppercase}
.welcome-text{left:128px;top:870px;width:215px;font-size:13px;line-height:15.5px;color:var(--text-muted)}
.read-more{left:128px;top:962px;font-size:13px;color:var(--text-light)}
.update{width:280px;height:100px}
.update .date{position:absolute;left:0;top:0;width:79px;height:79px;border:1px solid #444;border-radius:50%;display:flex;align-items:center;justify-content:center;font-size:16px;color:var(--text-light)}
.update .title{position:absolute;left:97px;top:0;font-size:13px;color:var(--text-light)}
.update .body{position:absolute;left:97px;top:19px;width:190px;font-size:12px;line-height:14px;color:var(--text-muted)}
.update-rule{height:1px;background:var(--line)}
.more-updates{right:115px;top:940px;font-size:12px;color:var(--text-light)}

.mailing-band{left:0;top:1046px;width:1093px;height:73px;background:var(--red-band)}
.mailing-band .brand{left:119px;top:21px}
.mailing-band .brand-name,.mailing-band .brand-dot{color:#c8cbcf}
.mailing-band .brand-dot{background:#c8cbcf}
.mailing-title{left:493px;top:16px;font-family:"Oswald",sans-serif;font-weight:300;font-size:30px;line-height:1;color:#d9dbde;text-transform:uppercase;letter-spacing:-.5px}
.mail-form{left:731px;top:18px;width:246px;height:38px;background:var(--red-dark);border:2px solid #c00000;display:flex}
.mail-form .field{flex:1;padding:10px 10px;font-size:13px;color:#e06060}
.mail-form .go{width:62px;background:var(--red);font-family:"Teko",sans-serif;font-weight:600;font-size:30px;line-height:36px;color:#fff;text-align:center}

.site-footer{left:0;top:1119px;width:1093px;height:81px;background:var(--footer)}
.footer-nav{left:120px;top:37px;display:flex;gap:12px;font-size:11px;color:var(--text-light)}
.social{right:124px;top:30px;display:flex;gap:7px}
.social span{width:26px;height:26px;border-radius:50%;background:#a6a9ad}
</style>
</head>
<body>
  <div class="abs top-strip"></div>
  <header class="abs site-header">
    <div class="abs brand"><span class="brand-dot"></span><span class="brand-name">Harbor Bolts</span></div>
    <nav class="abs main-nav"><span class="active">Home</span><span>About Us</span><span>Products</span><span>Services</span><span>Blog</span><span>Contact Us</span></nav>
  </header>
  <div class="abs nav-marker"></div>

  <section>
    <div class="abs hero-photo" role="img" aria-label="Photo of a man in a dark shirt opening a door onto bright light"></div>
    <h1 class="abs hero-copy"><div class="l1">Keeper of the Gate</div><div class="l2">Professional</div><div class="l3">Strong</div><div class="l4">Reliable</div></h1>
  </section>

  <section class="abs product-band"></section>
  <svg class="abs carousel-btn" style="left:105px" viewBox="0 0 30 30"><circle cx="15" cy="15" r="13.5" fill="none" stroke="#000" stroke-width="2.5"/><path d="M17.5 9 L11.5 15 L17.5 21" fill="none" stroke="#000" stroke-width="3"/></svg>
  <svg class="abs carousel-btn" style="left:962px" viewBox="0 0 30 30"><circle cx="15" cy="15" r="13.5" fill="none" stroke="#000" stroke-width="2.5"/><path d="M12.5 9 L18.5 15 L12.5 21" fill="none" stroke="#000" stroke-width="3"/></svg>
  <div class="abs product-strip">
    <article class="product"><div class="product-image knob" role="img" aria-label="Photo of a brass entry lock knob with key"></div><h2 class="product-title">Entry Lock</h2><p class="product-text">Lorem ipsum dolor sit amet, consectetur adipisicing elit, sed do eiusmod tempor incididunt ut.</p></article>
    <article class="product"><div class="product-image box" role="img" aria-label="Photo of a black combination lockbox with shackle"></div><h2 class="product-title">Lockbox</h2><p class="product-text">Lorem ipsum dolor sit amet, consectetur adipisicing elit, sed do eiusmod tempor incididunt ut.</p></article>
    <article class="product"><div class="product-image knob" role="img" aria-label="Photo of a brass entry lock knob with key"></div><h2 class="product-title">Entry Lock</h2><p class="product-text">Lorem ipsum dolor sit amet, consectetur adipisicing elit, sed do eiusmod tempor incididunt ut.</p></article>
    <article class="product"><div class="product-image box" role="img" aria-label="Photo of a black combination lockbox with shackle"></div><h2 class="product-title">Lockbox</h2><p class="product-text">Lorem ipsum dolor sit amet, consectetur adipisicing elit, sed do eiusmod tempor incididunt ut.</p></article>
  </div>

  <h2 class="abs welcome-title">Welcome</h2>
  <p class="abs welcome-text">Mes cuml dia sed in lacus ut eniascet ingerto aliiqt es site amet eismod ictor ut ligulate ameti dapibus ticdu nt mtsen lusto dolor ltissim com. Mes cuml dia sed inertio.</p>
  <a class="abs read-more">read more +</a>

  <div class="abs update" style="left:380px;top:821px"><div class="date">16.04</div><div class="title">Ut enim ad minim veniam, quis</div><p class="body">Excepteur sint occaecat cupidatat non proident, sunt in culpa qui officia eserunt mollit anim id est laborum.</p></div>
  <div class="abs update" style="left:695px;top:821px"><div class="date">16.04</div><div class="title">Ut enim ad minim veniam, quis</div><p class="body">Excepteur sint occaecat cupidatat non proident, sunt in culpa qui officia eserunt mollit anim id est laborum.</p></div>
  <div class="abs update-rule" style="left:383px;top:926px;width:278px"></div>
  <div class="abs update-rule" style="left:698px;top:926px;width:279px"></div>
  <a class="abs more-updates">+ more updates</a>

  <section class="abs mailing-band">
    <div class="abs brand"><span class="brand-dot"></span><span class="brand-name">Harbor Bolts</span></div>
    <div class="abs mailing-title">Join our mailing list</div>
    <div class="abs mail-form"><span class="field">Example@email.com</span><span class="go">GO</span></div>
  </section>

  <footer class="abs site-footer">
    <nav class="abs footer-nav"><span>Home</span><span>About Us</span><span>Products</span><span>Services</span><span>Blog</span><span>Contact</span><span>Legal</span><span>Privacy Policy</span><span>©2013 Meridian Hardware Group</span></nav>
    <div class="abs social"><span></span><span></span><span></span><span></span><span></span></div>
  </footer>
</body>
</html>
```